Ferris + Oakdale Architecture Ltd Stationary rebrand Lead designer to create a fresh clean modern...

We have recieved a great new logo design and now we are after a consistant fresh and modern stationary to match the new design. Business card design, Letter Head design, presentatnion folders and other stationery within the package. I have also added some of our existing layouts for presentation we would like updating with the new look, We would like a clean modern fresh design that looks visually pleasing on the page. we cant wait to see what you come up with!!!!

Target Market(s)

young professionals and middle age clients

Industry/Entity Type

Architect

Contact Information for Business Card

i have uploarded our orginal business card that has all the details attached.

Font styles to use
Sans Serif

Colors
000000
ffffff
d3d3d3

Requirements
Must have
• Logo and our contact information
Nice to have
• white sape around the card to give a clean look.

```html
<!DOCTYPE html>
<html lang="en">
<head>
<meta charset="utf-8">
<title>Ferris + Oakdale Architecture — Stationery</title>
<link href="https://fonts.googleapis.com/css2?family=Montserrat:wght@400;500;600&display=swap" rel="stylesheet">
<style>
  :root{
    --black:#000000;
    --ink:#1c1c1c;
    --white:#ffffff;
    --grey:#d3d3d3;
    --faint:#f6f6f6;
    --text:#111111;
  }
  *{margin:0;padding:0;box-sizing:border-box}
  html,body{width:1200px;height:1200px;overflow:hidden;background:var(--white)}
  body{position:relative;font-family:"Montserrat",Arial,sans-serif;color:var(--text)}
  .sheet{position:absolute;background:var(--white);box-shadow:0 8px 18px rgba(0,0,0,.28)}
  .card{width:325px;height:186px;left:71px}
  .card--dark{top:174px;height:195px;background:var(--ink)}
  .card--bar{top:412px}
  .card--plain{top:645px}
  .card--split{top:878px}
  .letterhead{left:446px;top:174px;width:688px;height:890px}

  .brand{display:flex;align-items:center;gap:8px;position:absolute}
  .brand__square{width:14px;height:14px;background:var(--black);flex:none}
  .brand__name{font-weight:500;text-transform:uppercase;line-height:1.35;color:var(--black)}
  .brand__name span{display:block;letter-spacing:.42em}
  .card--dark .brand{left:0;right:0;top:70px;justify-content:center}
  .card--dark .brand__square{background:var(--grey)}
  .card--dark .brand__name{color:var(--grey);font-size:10px;letter-spacing:.08em}
  .card--dark .brand__name span{font-size:6px}

  .tag{position:absolute;right:14px;top:14px;font-size:8px;font-weight:500;letter-spacing:.08em;color:var(--black);text-transform:uppercase;text-align:right;line-height:1.4}

  .person{position:absolute}
  .person__name{font-size:13px;font-weight:600;letter-spacing:.02em}
  .person__role{font-size:8px;letter-spacing:.2em;margin-top:1px}
  .contacts{position:absolute;list-style:none}
  .contacts li{display:flex;align-items:center;gap:14px;font-size:7.6px;line-height:1.3;margin-bottom:8px}
  .icon{width:14px;height:14px;background:var(--black);display:flex;align-items:center;justify-content:center;flex:none}
  .icon svg{width:9px;height:9px;fill:var(--white)}

  .card--bar .person{left:13px;top:59px}
  .card--bar .contacts{left:13px;top:99px}
  .bar{position:absolute;bottom:0;height:5px}
  .bar--black{left:0;width:245px;background:var(--black)}
  .bar--grey{left:253px;right:0;background:var(--grey)}
  .card--plain .person{left:21px;top:55px}
  .card--plain .contacts{left:21px;top:94px}

  .split__brand{position:absolute;left:18px;top:72px;width:150px}
  .split__brand .brand{position:static;justify-content:center}
  .split__brand .brand__name{font-size:10px;letter-spacing:.06em}
  .split__brand .brand__name span{font-size:6px}
  .split__rule{position:absolute;left:172px;top:30px;width:1px;height:138px;background:#555}
  .split__info{position:absolute;left:182px;top:27px;font-size:7.3px;line-height:1.3}
  .split__info .person{position:static}
  .split__info .person__name{font-size:12.5px}
  .split__info .person__role{font-size:7px;margin-bottom:10px}
  .split__info p{margin-bottom:5px}
  .mini{list-style:none;margin-top:9px}
  .mini li{display:flex;align-items:center;gap:4px;font-size:7px;line-height:1.55}
  .mini svg{width:6px;height:6px;fill:var(--black)}

  .letterhead .brand{left:0;right:0;top:76px;justify-content:center;gap:12px}
  .letterhead .brand__square{width:22px;height:22px}
  .letterhead .brand__name{font-size:15px;letter-spacing:.08em}
  .letterhead .brand__name span{font-size:8px}
  .backdrop{position:absolute;left:151px;top:368px;width:385px;height:385px;background:var(--faint)}
  .footer{position:absolute;left:40px;right:40px;top:825px;display:flex;justify-content:space-between;list-style:none}
  .footer li{display:flex;align-items:center;gap:16px;font-size:12.5px;line-height:1.2;letter-spacing:.02em}
  .footer .icon{width:22px;height:22px}
  .footer .icon svg{width:14px;height:14px}
</style>
</head>
<body>
<svg width="0" height="0" style="position:absolute">
  <defs>
    <symbol id="i-phone" viewBox="0 0 24 24"><path d="M6.6 10.8a15.1 15.1 0 0 0 6.6 6.6l2.2-2.2a1 1 0 0 1 1-.25 11.4 11.4 0 0 0 3.6.57 1 1 0 0 1 1 1V20a1 1 0 0 1-1 1A17 17 0 0 1 3 4a1 1 0 0 1 1-1h3.5a1 1 0 0 1 1 1c0 1.25.2 2.45.57 3.57a1 1 0 0 1-.25 1z"/></symbol>
    <symbol id="i-globe" viewBox="0 0 24 24"><path d="M12 2a10 10 0 1 0 0 20 10 10 0 0 0 0-20zm0 2c.9 0 2.1 1.7 2.7 5H9.3C9.9 5.7 11.1 4 12 4zM4.3 11h3c0 .7 0 1.3.1 2H4.3a8 8 0 0 1 0-2zm.8 4h2.6c.3 1.5.8 2.8 1.4 3.8A8 8 0 0 1 5.1 15zm2.6-6H5.1a8 8 0 0 1 4-3.8C8.5 6.2 8 7.5 7.7 9zM12 20c-.9 0-2.1-1.7-2.7-5h5.4c-.6 3.3-1.8 5-2.7 5zm-2.9-7a19 19 0 0 1 0-2h5.8a19 19 0 0 1 0 2zm5.8 5.8c.6-1 1.1-2.3 1.4-3.8h2.6a8 8 0 0 1-4 3.8zM16.7 13c.1-.7.1-1.3.1-2h3a8 8 0 0 1 0 2zm-.4-4c-.3-1.5-.8-2.8-1.4-3.8a8 8 0 0 1 4 3.8z"/></symbol>
    <symbol id="i-pin" viewBox="0 0 24 24"><path d="M12 2a7 7 0 0 0-7 7c0 5.2 7 13 7 13s7-7.8 7-13a7 7 0 0 0-7-7zm0 9.5A2.5 2.5 0 1 1 12 6.5a2.5 2.5 0 0 1 0 5z"/></symbol>
    <symbol id="i-mobile" viewBox="0 0 24 24"><path d="M7 1h10a2 2 0 0 1 2 2v18a2 2 0 0 1-2 2H7a2 2 0 0 1-2-2V3a2 2 0 0 1 2-2zm0 3v15h10V4z"/></symbol>
    <symbol id="i-mail" viewBox="0 0 24 24"><path d="M2 5h20v14H2zm2 2v.5l8 5 8-5V7z"/></symbol>
  </defs>
</svg>

<section class="sheet card card--dark">
  <div class="brand">
    <div class="brand__square"></div>
    <div class="brand__name">Ferris + Oakdale<span>Architecture</span></div>
  </div>
</section>

<section class="sheet card card--bar">
  <div class="tag">Ferris + Oakdale</div>
  <div class="person"><div class="person__name">DANIEL FERRIS</div><div class="person__role">Director</div></div>
  <ul class="contacts">
    <li><span class="icon"><svg><use href="#i-phone"/></svg></span><span>03 555 0142<br>0274 555 019</span></li>
    <li><span class="icon"><svg><use href="#i-globe"/></svg></span><span>daniel@foarchitecture.co.nz<br>www.foarchitecture.co.nz</span></li>
    <li><span class="icon"><svg><use href="#i-pin"/></svg></span><span>12 Harlow Street, Millbrook 7700<br>PO Box 4410, Millbrook 7740</span></li>
  </ul>
  <div class="bar bar--black"></div><div class="bar bar--grey"></div>
</section>

<section class="sheet card card--plain">
  <div class="tag">Ferris + Oakdale</div>
  <div class="person"><div class="person__name">DANIEL FERRIS</div><div class="person__role">Director</div></div>
  <ul class="contacts">
    <li><span class="icon"><svg><use href="#i-phone"/></svg></span><span>03 555 0142<br>0274 555 019</span></li>
    <li><span class="icon"><svg><use href="#i-globe"/></svg></span><span>daniel@foarchitecture.co.nz<br>www.foarchitecture.co.nz</span></li>
    <li><span class="icon"><svg><use href="#i-pin"/></svg></span><span>12 Harlow Street, Millbrook 7700<br>PO Box 4410, Millbrook 7740</span></li>
  </ul>
</section>

<section class="sheet card card--split">
  <div class="split__brand">
    <div class="brand">
      <div class="brand__square"></div>
      <div class="brand__name">Ferris + Oakdale<span>Architecture</span></div>
    </div>
  </div>
  <div class="split__rule"></div>
  <div class="split__info">
    <div class="person"><div class="person__name">DANIEL FERRIS</div><div class="person__role">Director</div></div>
    <p>12 Harlow Street<br>Millbrook 7700</p>
    <p>PO Box 4410<br>Millbrook 7740</p>
    <ul class="mini">
      <li><svg><use href="#i-phone"/></svg>03 555 0142</li>
      <li><svg><use href="#i-mobile"/></svg>0274 555 019</li>
      <li><svg><use href="#i-mail"/></svg>daniel@foarchitecture.co.nz</li>
      <li><svg><use href="#i-globe"/></svg>www.foarchitecture.co.nz</li>
    </ul>
  </div>
</section>

<section class="sheet letterhead">
  <div class="brand">
    <div class="brand__square"></div>
    <div class="brand__name">Ferris + Oakdale<span>Architecture</span></div>
  </div>
  <div class="backdrop"></div>
  <ul class="footer">
    <li><span class="icon"><svg><use href="#i-phone"/></svg></span><span>03 555 0142<br>0274 555 019</span></li>
    <li><span class="icon"><svg><use href="#i-globe"/></svg></span><span>daniel@foarchitecture.co.nz<br>www.foarchitecture.co.nz</span></li>
    <li><span class="icon"><svg><use href="#i-pin"/></svg></span><span>12 Harlow Street, Millbrook 7700<br>PO Box 4410, Millbrook 7740</span></li>
  </ul>
</section>
</body>
</html>
```